The hardcover "Star Chronicle" (large size, Quarto 4º, 12 × 9 1/2 in, 30.5 × 24.15 cm) in German language as follows:

STERNENCHRONIK (title)
der herausragendsten Unternehmer und Manager Deutschlands 2013 (subtitle 1)
BERLIN UND BRANDENBURG (subtitle 2, smaller than subtitle 1)

Morvalto (logo, WMF file attached)
Updates

Reason: The solutions are rather too childish and pre-made styles... is there anyone who can make it better? - a professional-looking business book (encyclopedia style, should have no color-pictures, no author's name, logo smaller due to the large size book)

Target Market(s)

business community

Requirements
Must have
• encyclopedia style large size book
must look professional and expensive

Nice to have
• - gold-color hardcover, or some gold-color elements
- some simple and decent graphic element (e.g. an ancient column, or some other architectural detail), if any
Should not have
• no color-pictures
no author's name

```html
<!DOCTYPE html>
<html lang="de">
<head>
<meta charset="utf-8">
<title>Sternenchronik 2013 – Einband</title>
<link rel="stylesheet" href="https://fonts.googleapis.com/css2?family=Barlow+Semi+Condensed:wght@500;600&family=Barlow:wght@500;700&display=swap">
<style>
  :root {
    --page: #ffffff;
    --cover: #000000;
    --gold: #f7941d;
    --gold-deep: #d9780c;
  }
  html, body {
    margin: 0;
    padding: 0;
    width: 1056px;
    height: 1200px;
    overflow: hidden;
    background: var(--page);
  }
  .book-jacket {
    display: block;
    width: 1056px;
    height: 1200px;
  }
  .cover-board, .spine-board { fill: var(--cover); }
  .column-illustration { fill: url(#columnTone); }
  .title {
    font-family: "Barlow Semi Condensed", "Arial Narrow", sans-serif;
    font-weight: 500;
    fill: var(--gold);
  }
  .subtitle {
    font-family: "Barlow", Arial, sans-serif;
    font-weight: 500;
    fill: var(--gold);
  }
  .publisher {
    font-family: "Barlow", Arial, sans-serif;
    font-weight: 700;
    fill: var(--gold);
  }
</style>
</head>
<body>
<svg class="book-jacket" viewBox="0 0 1056 1200" xmlns="http://www.w3.org/2000/svg">
  <defs>
    <linearGradient id="columnTone" x1="0" x2="1" y1="0" y2="0">
      <stop offset="0" stop-color="var(--gold-deep)"/>
      <stop offset="0.5" stop-color="var(--gold)"/>
      <stop offset="1" stop-color="var(--gold-deep)"/>
    </linearGradient>
  </defs>

  <!-- Front cover -->
  <g class="front-cover">
    <rect class="cover-board" x="0" y="0" width="888" height="1125"/>

    <rect class="column-illustration" x="58" y="207" width="208" height="882"
          role="img" aria-label="Ionische Säule mit Volutenkapitell, kanneliertem Schaft und Basis"/>

    <text class="title title-line-1" x="78" y="175" font-size="172"
          textLength="752" lengthAdjust="spacingAndGlyphs">STERNEN</text>
    <text class="title title-line-2" x="272" y="363" font-size="238"
          textLength="469" lengthAdjust="spacingAndGlyphs">CHRONIK</text>
    <text class="title title-year" transform="translate(834 369) rotate(-90)" font-size="86"
          textLength="175" lengthAdjust="spacingAndGlyphs">2013</text>

    <text class="subtitle subtitle-main" x="266" y="430" font-size="44"
          textLength="566" lengthAdjust="spacingAndGlyphs">DER HERAUSRAGENDSTEN</text>
    <text class="subtitle subtitle-main" x="266" y="477" font-size="44"
          textLength="379" lengthAdjust="spacingAndGlyphs">UNTERNEHM UND</text>
    <text class="subtitle subtitle-main" x="266" y="524" font-size="44"
          textLength="576" lengthAdjust="spacingAndGlyphs">MANAGER DEUTSCHLANDS</text>

    <text class="subtitle subtitle-region" x="266" y="654" font-size="44"
          textLength="579" lengthAdjust="spacingAndGlyphs">BERLIN UND BRANDENBUR</text>

    <text class="publisher" x="682" y="1094" font-size="22"
          textLength="121" lengthAdjust="spacingAndGlyphs">Morvalto</text>
  </g>

  <!-- Spine -->
  <g class="spine">
    <rect class="spine-board" x="905" y="0" width="141" height="1125"/>

    <text class="title spine-year" transform="translate(958 58) rotate(90)" font-size="86"
          textLength="137" lengthAdjust="spacingAndGlyphs">2013</text>
    <text class="title spine-title" transform="translate(1030 1011) rotate(-90)" font-size="126"
          textLength="765" lengthAdjust="spacingAndGlyphs">STERNENCHRONIK</text>

    <text class="publisher" x="934" y="1095" font-size="17"
          textLength="94" lengthAdjust="spacingAndGlyphs">Morvalto</text>
  </g>
</svg>
</body>
</html>
```